Holvern Incorporated

Holvern is a business that provides consulting, and manages and supplies trades persons in the construction and heavy industries sector. We build, do maintenance, install machinery, and can manage projects or jobs. Would like or prefer more clean, classic designs. Blacks/greys, but open to almost anything.

Target Market(s)

Industrial/Construction/Manufacturing

Industry/Entity Type

Construction Company

Contact Information for Business Card

Clean, business name on the front, possibly have the details on the back, but open to any ideas.

Logo Text

We currently do not have a slogan, open to ideas

Font styles to use
Serif
Sans Serif

Colors

Designer to choose colors to be used in the design.

Requirements
Should not have
• the oval is not my logo, was just an idea. please don't send 20 designs with the oval

```html
<!DOCTYPE html>
<html lang="en">
<head>
<meta charset="utf-8">
<title>Holvern Incorporated — Business Card</title>
<link href="https://fonts.googleapis.com/css2?family=Open+Sans:wght@400;600&display=swap" rel="stylesheet">
<style>
  :root {
    --stage: #d6d6d6;
    --ink: #0b0b0b;
    --paper: #ffffff;
    --text-dark: #1c1c1c;
    --text-mid: #3a3a3a;
    --shadow: rgba(0, 0, 0, 0.22);
  }
  * { margin: 0; padding: 0; box-sizing: border-box; }
  html, body {
    width: 1200px;
    height: 900px;
    overflow: hidden;
    background: var(--stage);
    font-family: "Open Sans", sans-serif;
  }
  .stage {
    position: relative;
    width: 1200px;
    height: 900px;
  }
  .card {
    position: absolute;
    width: 560px;
    height: 320px;
    box-shadow: 0 6px 18px var(--shadow);
  }
  .card--front {
    left: 70px;
    top: 100px;
    background: var(--ink);
    display: flex;
    align-items: center;
    justify-content: center;
  }
  .card--back {
    left: 570px;
    top: 480px;
    background: var(--paper);
    display: flex;
    align-items: center;
  }
  .brand-name {
    font-family: "Open Sans", sans-serif;
    font-weight: 600;
    letter-spacing: 0.5px;
  }
  .card--front .brand-name {
    color: var(--paper);
    font-size: 40px;
  }
  .card--back .brand-block {
    width: 250px;
    display: flex;
    justify-content: center;
  }
  .card--back .brand-name {
    color: var(--ink);
    font-size: 24px;
    text-align: center;
    line-height: 1.25;
  }
  .details {
    padding-left: 20px;
    color: var(--text-mid);
    font-size: 14px;
    line-height: 1.45;
  }
  .details .person-name {
    color: var(--text-dark);
    font-weight: 600;
    font-size: 18px;
    line-height: 1.2;
  }
  .details .person-role {
    margin-bottom: 14px;
  }
  .contact-line {
    display: flex;
    align-items: center;
    gap: 6px;
  }
  .contact-line svg {
    width: 12px;
    height: 12px;
    flex: none;
  }
</style>
</head>
<body>
  <main class="stage">
    <section class="card card--front">
      <span class="brand-name">Holvern Incorporated</span>
    </section>

    <section class="card card--back">
      <div class="brand-block">
        <span class="brand-name">Holvern<br>Incorporated</span>
      </div>
      <div class="details">
        <p class="person-name">Daniel Ashford</p>
        <p class="person-role">President</p>
        <p>48 Carden Row, Suite 310</p>
        <p>Tarrow, Ohio, 44907</p>
        <p class="contact-line">
          <svg viewBox="0 0 12 12" aria-hidden="true"><path d="M2.5 1 L4.5 1 L5 3.5 L3.8 4.4 Q4.8 6.8 7.4 8.2 L8.4 7 L11 7.5 L11 9.5 Q10.5 11 9 11 Q1 10 1 2.5 Q1 1.2 2.5 1 Z" fill="#1c1c1c"/></svg>
          (555) 214-6380
        </p>
        <p class="contact-line">
          <svg viewBox="0 0 12 12" aria-hidden="true"><rect x="0.8" y="2.3" width="10.4" height="7.4" fill="none" stroke="#1c1c1c" stroke-width="1.2"/><path d="M0.8 2.5 L6 6.6 L11.2 2.5" fill="none" stroke="#1c1c1c" stroke-width="1.2"/></svg>
          daniel@holvern.com
        </p>
        <p class="contact-line">
          <svg viewBox="0 0 12 12" aria-hidden="true"><circle cx="6" cy="6" r="5.2" fill="#1c1c1c"/><path d="M0.8 6 H11.2 M6 0.8 Q3 6 6 11.2 M6 0.8 Q9 6 6 11.2" fill="none" stroke="#fff" stroke-width="0.8"/></svg>
          www.holvern.com
        </p>
      </div>
    </section>
  </main>
</body>
</html>
```